I'd like a business card that makes my company, Harwick Denton Associates Ltd stand out from the normal financial & IT services sector . It would be great to have a card that a potential client will think "wow" this is out of the norm , I'll give these guys a call. My business aims to provide consultancy services for financial and IT institutions but I'm looking to provide a newer approach that fits into today's social media rather than the standard "big 4" approach. My business helps companies assess their internal issues and aims to solve issues via business process re-engineering. The final design should have a balance of the maturity of the financial & IT sector with the fresh approach of the thriving social media sector

Target Market(s)

Business Managers and Directors, technical Managers and directors. Aged between 20 and 60 that handle project budgets

Industry/Entity Type

Financial

Requirements
Must have
• Must incorporate company logo currently being designed
Should not have
• No old-style fonts please.

```html
<!DOCTYPE html>
<html lang="en">
<head>
<meta charset="UTF-8">
<title>Harwick Denton Associates Ltd — Business Card</title>
<link rel="stylesheet" href="https://fonts.googleapis.com/css2?family=Open+Sans:wght@400;600;700&display=swap">
<style>
  :root {
    --stage: #2b2826;
    --card-front: #1c1c1c;
    --card-back: #0d0d0d;
    --emboss: #303030;
    --emboss-light: #3a3a3a;
    --magenta: #b0407f;
    --orange: #f07a2c;
    --ink: #f2f2f2;
    --ink-soft: #d8d8d8;
  }
  * { box-sizing: border-box; margin: 0; padding: 0; }
  html, body {
    width: 1200px; height: 716px; overflow: hidden;
    background: var(--stage);
    font-family: "Open Sans", Arial, sans-serif;
  }
  .canvas {
    position: relative; width: 1200px; height: 716px;
    display: flex; align-items: center; justify-content: center; gap: 50px;
  }
  .card {
    width: 500px; height: 286px; position: relative;
    box-shadow: 0 18px 40px rgba(0,0,0,.55);
  }

  /* Front side */
  .card--front {
    background: var(--card-front);
    display: flex; align-items: center; justify-content: center; gap: 18px;
  }
  .front-mark {
    width: 54px; height: 54px; background: var(--emboss);
  }
  .front-wordmark { color: var(--emboss-light); }
  .front-wordmark__name {
    font-weight: 600; font-size: 27px; letter-spacing: 2px; text-transform: uppercase;
    line-height: 1.1;
  }
  .front-wordmark__sub {
    font-weight: 600; font-size: 14px; letter-spacing: 3px; text-align: right; margin-top: 4px;
  }

  /* Back side */
  .card--back {
    background: var(--card-back);
    display: flex; align-items: center; padding-left: 44px;
  }
  .back-brand {
    width: 170px; display: flex; flex-direction: column; align-items: flex-start; gap: 12px;
  }
  .back-brand__square { width: 96px; height: 96px; background: var(--orange); }
  .back-brand__name {
    color: var(--orange); font-weight: 700; font-size: 15px; letter-spacing: .5px;
    text-transform: uppercase; line-height: 1.2;
  }
  .divider {
    width: 2px; height: 150px; background: var(--magenta); margin: 0 22px 0 14px;
  }
  .contact { color: var(--ink); }
  .contact__name {
    color: var(--orange); font-weight: 700; font-size: 17px; letter-spacing: .5px; text-transform: uppercase;
  }
  .contact__role { font-size: 11px; color: var(--ink-soft); margin-bottom: 14px; }
  .contact__list { list-style: none; }
  .contact__item {
    display: flex; align-items: center; gap: 8px; font-size: 12.5px; line-height: 20px;
  }
  .contact__icon { width: 12px; height: 12px; flex: none; }
  .contact__address {
    color: var(--orange); font-size: 11.5px; margin-top: 10px; text-transform: uppercase; letter-spacing: .2px;
  }
</style>
</head>
<body>
<main class="canvas">
  <section class="card card--front" aria-label="Card front">
    <div class="front-mark"></div>
    <div class="front-wordmark">
      <div class="front-wordmark__name">Harwick Denton</div>
      <div class="front-wordmark__sub">Associates Ltd</div>
    </div>
  </section>

  <section class="card card--back" aria-label="Card back">
    <div class="back-brand">
      <div class="back-brand__square"></div>
      <div class="back-brand__name">Harwick Denton</div>
    </div>
    <div class="divider"></div>
    <div class="contact">
      <h1 class="contact__name">Samir K. Nadeem</h1>
      <p class="contact__role">Director</p>
      <ul class="contact__list">
        <li class="contact__item">
          <svg class="contact__icon" viewBox="0 0 12 12" aria-hidden="true"><rect width="12" height="12" rx="1.5" fill="var(--magenta)"/><path d="M3.5 2.5h1.6l.7 2-1 .8a5 5 0 0 0 1.9 1.9l.8-1 2 .7v1.6c0 .5-.4.9-.9.9A6.6 6.6 0 0 1 2.6 3.4c0-.5.4-.9.9-.9z" fill="#0d0d0d"/></svg>
          +(965) 55012870
        </li>
        <li class="contact__item">
          <svg class="contact__icon" viewBox="0 0 12 12" aria-hidden="true"><rect width="12" height="12" rx="1.5" fill="var(--magenta)"/><path d="M3.5 2.5h1.6l.7 2-1 .8a5 5 0 0 0 1.9 1.9l.8-1 2 .7v1.6c0 .5-.4.9-.9.9A6.6 6.6 0 0 1 2.6 3.4c0-.5.4-.9.9-.9z" fill="#0d0d0d"/></svg>
          +(971) 550198273
        </li>
        <li class="contact__item">
          <svg class="contact__icon" viewBox="0 0 12 12" aria-hidden="true"><rect width="12" height="12" rx="1.5" fill="var(--magenta)"/><rect x="2.5" y="3.5" width="7" height="5" fill="none" stroke="#0d0d0d" stroke-width="1"/><path d="M2.5 3.5 6 6.5l3.5-3" fill="none" stroke="#0d0d0d" stroke-width="1"/></svg>
          samir@harwickdenton.com
        </li>
      </ul>
      <p class="contact__address">P.O. Box 2781 Safat, Kuwait 13028</p>
    </div>
  </section>
</main>
</body>
</html>
```